Corvallin Property Solutions need a business card design

Hello guys. We would need a business card design asap please.
We are a start up property investment business based in London UK specialised in buying, selling, managing and letting properties and helping distressed property owners.
The name of our Business is Corvallin, the logo symbolises the four fundamental elements of the world (earth, air, fire and water) and so it stands for strength, stability, longevity.
We would like the business card to communicate professionalism and reliability. Many many thanks indeed for your work.

Details:

1.) Marisol Dunkley
Property Investor
Mobile: +44(0)7700362517
Email: marisol.corvallin@quilbrook.example

2.) Tomas Brindle
Property Investor
Mobile: +44(0)7700845926
Email: tomas.corvallin@quilbrook.example

Industry/Entity Type

Investment

```html
<!DOCTYPE html>
<html lang="en">
<head>
<meta charset="utf-8">
<title>Corvallin Property Solutions – Business Card</title>
<link rel="stylesheet" href="https://fonts.googleapis.com/css2?family=Jost:wght@500;700&family=Open+Sans:wght@400;600&display=swap">
<style>
  :root {
    --backdrop: #d3d3d5;
    --card: #ffffff;
    --green: #168a45;
    --green-soft: #3aa866;
    --blue: #2b5fae;
    --blue-soft: #4a86cf;
    --red: #cf2030;
    --brand-grey: #8c8c8c;
    --ghost: #ededed;
    --text-light: #ffffff;
  }
  * { box-sizing: border-box; margin: 0; padding: 0; }
  html, body {
    width: 883px; height: 1200px; overflow: hidden;
    background: var(--backdrop);
  }
  .sheet { position: relative; width: 883px; height: 1200px; }
  .card {
    position: absolute; left: 267px; width: 390px; overflow: hidden;
    box-shadow: 0 3px 8px rgba(0,0,0,.18);
  }

  /* Front */
  .card--front { top: 687px; height: 218px; }
  .front-art {
    position: absolute; inset: 0;
    background: linear-gradient(90deg, var(--green) 0%, var(--green-soft) 40%, var(--blue-soft) 60%, var(--blue) 100%);
  }
  .front-brand {
    position: absolute; right: 17px; bottom: 10px; text-align: center;
    font-family: "Jost", sans-serif; font-weight: 700; color: var(--brand-grey);
    opacity: .9;
  }
  .front-brand__name { font-size: 26px; letter-spacing: .5px; line-height: 1; }
  .front-brand__tag { font-size: 12px; letter-spacing: .6px; margin-top: 5px; }

  /* Back */
  .card--back { top: 921px; height: 203px; background: var(--card); }
  .ghost-name {
    position: absolute; left: 152px; top: 30px;
    font-family: "Jost", sans-serif; font-weight: 700; color: var(--ghost);
    line-height: 1; white-space: nowrap;
  }
  .ghost-name__name { font-size: 34px; }
  .ghost-name__tag { font-size: 17px; margin-top: 8px; margin-left: 30px; }
  .brand {
    position: absolute; left: 22px; top: 24px; width: 120px; text-align: center;
    font-family: "Jost", sans-serif; font-weight: 700; color: var(--brand-grey);
  }
  .brand__mark {
    display: block; width: 46px; height: 46px; margin: 0 auto 22px;
    border-radius: 50%; background: var(--brand-grey);
  }
  .brand__name { font-size: 16px; letter-spacing: .4px; line-height: 1; }
  .brand__tag { font-size: 7px; letter-spacing: .4px; margin-top: 4px; }

  .details {
    position: absolute; left: 18px; top: 130px; width: 353px;
    font-family: "Open Sans", sans-serif; color: var(--text-light);
    display: flex; flex-direction: column; gap: 3px;
  }
  .details__row { display: flex; align-items: center; padding-left: 14px; }
  .details__row--name { background: var(--red); height: 23px; padding-left: 10px; }
  .details__row--phone { background: var(--blue); height: 14px; }
  .details__row--email { background: var(--green); height: 14px; }
  .person-name { font-size: 12.5px; }
  .person-divider { width: 1px; height: 14px; background: var(--text-light); margin: 0 8px; }
  .person-role { font-size: 10px; }
  .contact { font-size: 9.5px; margin-left: 8px; }
  .icon { width: 9px; height: 9px; flex: none; }

  .colour-strip {
    position: absolute; left: 220px; right: 0; bottom: 0; height: 10px;
    display: flex;
  }
  .colour-strip span { flex: 1; }
  .colour-strip .green { background: var(--green); }
  .colour-strip .blue { background: var(--blue); }
  .colour-strip .red { background: var(--red); }
</style>
</head>
<body>
<main class="sheet">
  <section class="card card--front">
    <div class="front-art" role="img" aria-label="Large brand artwork in green, blue and red with a bright central glow"></div>
    <div class="front-brand">
      <div class="front-brand__name">CORVALLIN</div>
      <div class="front-brand__tag">PROPERTY SOLUTIONS</div>
    </div>
  </section>

  <section class="card card--back">
    <div class="ghost-name" aria-hidden="true">
      <div class="ghost-name__name">CORVALLIN</div>
      <div class="ghost-name__tag">PROPERTY SOLUTIONS</div>
    </div>

    <div class="brand">
      <span class="brand__mark"></span>
      <div class="brand__name">CORVALLIN</div>
      <div class="brand__tag">PROPERTY SOLUTIONS</div>
    </div>

    <div class="details">
      <div class="details__row details__row--name">
        <span class="person-name">Marisol Dunkley</span>
        <span class="person-divider"></span>
        <span class="person-role">Property Investor</span>
      </div>
      <div class="details__row details__row--phone">
        <svg class="icon" viewBox="0 0 10 10" aria-hidden="true"><rect x="2.5" y="0.5" width="5" height="9" rx="1" fill="none" stroke="#fff" stroke-width="1"/><line x1="4.3" y1="8" x2="5.7" y2="8" stroke="#fff" stroke-width="0.8"/></svg>
        <span class="contact">+44(0)7700362517</span>
      </div>
      <div class="details__row details__row--email">
        <svg class="icon" viewBox="0 0 10 10" aria-hidden="true"><rect x="0.5" y="2" width="9" height="6" fill="#fff"/><polyline points="0.5,2 5,5.5 9.5,2" fill="none" stroke="#168a45" stroke-width="0.9"/></svg>
        <span class="contact">marisol.corvallin@quilbrook.example</span>
      </div>
    </div>

    <div class="colour-strip" aria-hidden="true">
      <span class="green"></span><span class="blue"></span><span class="red"></span>
    </div>
  </section>
</main>
</body>
</html>
```